Brightwell Commercial Cleaning - Company OverView

I require a 3 page, A4 company folding proschure. I would like to convey a eco frienddly and professional service. Text and images can be found on our company web page www.brightwellcleaning.com.au however we may need some more eco friendly images to convey the right message

The broschure must highlight our companys ISO certification. We are a professional service targeting the corporate industry.

I have hi res images to send and also endorsement and certification logos to send through.

Designer may need to suppl;y some contact and images.

We would like to work with someoe frquently
Updates

HI TEAM, I AM SORRY FOR ANY CONFUSION. I HAVE JUST HAD INSTRUCTIONS THAT THE BROSCHURE WILL NEED TO BE AN A3 SIZE BUT DESIGNED WITH 2 A4 PAGES FRONT AND BACK. SORRY FOR ANY INCONVENIENCE

Target Market(s)

* Corporate
* Professional

Industry/Entity Type

Professional Service

Requirements
Must have
• * Environmental Feel
* Strong Prescense
* Must be CLEAN
* Have 6 A4 pages (Must be a 3 page a4 broschure, Double sided).
Should not have
• * Busy Text
* Old Font

```html
<!DOCTYPE html>
<html lang="en">
<head>
<meta charset="utf-8">
<title>Brightwell Commercial Cleaning – Company Overview</title>
<link href="https://fonts.googleapis.com/css2?family=Arimo:ital,wght@0,400;0,700;1,700&display=swap" rel="stylesheet">
<style>
  :root{
    --text-blue:#1f5fd6;
    --panel-blue:#4c8fe0;
    --white:#ffffff;
    --leaf-light:#b9e35a;
    --leaf-dark:#3f9a1c;
    --sky:#2f7fd8;
    --cert-blue:#2a5db8;
    --cert-green:#2ea03a;
    --cert-red:#d8304a;
    --logo-blue:#3a6fc4;
  }
  *{margin:0;padding:0;box-sizing:border-box}
  html,body{width:1200px;height:566px;overflow:hidden;background:#fff}
  body{font-family:"Arimo",Arial,sans-serif}
  .spread{position:relative;width:1200px;height:566px;overflow:hidden}

  /* left panel */
  .panel-left{position:absolute;left:0;top:0;width:398px;height:566px;
    background:linear-gradient(90deg,#e4f3fb 0%,#ffffff 60%)}
  .copy{position:absolute;left:42px;width:330px;color:var(--text-blue);font-size:9.6px;line-height:1.3}
  .copy p{margin-bottom:10px}
  .copy-top{top:34px}
  .copy-bottom{top:432px}
  .tree-photo{position:absolute;left:62px;top:222px;width:226px;height:192px;
    background:radial-gradient(ellipse at 50% 38%,#5fae2a 0%,#3f8f1c 45%,rgba(63,143,28,0) 72%),
               radial-gradient(ellipse at 50% 95%,rgba(120,120,120,.35) 0%,rgba(255,255,255,0) 40%)}

  /* middle panel */
  .panel-middle{position:absolute;left:398px;top:0;width:402px;height:566px;background:var(--panel-blue)}
  .leaf-photo{position:absolute;left:0;top:0;width:402px;height:236px;
    background:radial-gradient(ellipse at 70% 25%,#d8f07a 0%,var(--leaf-light) 30%,#6cc02c 65%,var(--leaf-dark) 100%)}
  .principles-intro{position:absolute;left:42px;top:259px;width:340px;color:var(--white);font-weight:700;font-size:9.2px;line-height:1.35}
  .principles{position:absolute;left:56px;top:298px;list-style:none;color:var(--white);font-size:9.2px}
  .principles li{display:flex;align-items:center;height:16.4px}
  .principles svg{width:12px;height:12px;margin-right:7px}
  .principles-outro{position:absolute;left:42px;top:398px;width:330px;color:var(--white);font-size:9.2px;line-height:1.3}
  .cert-box{position:absolute;left:39px;top:451px;width:324px;height:93px;background:var(--white);border-radius:8px;text-align:center}
  .cert-title{margin-top:8px;font-weight:700;font-size:9.6px;color:#1d3f8a}
  .cert-badges{display:flex;justify-content:center;gap:14px;margin-top:9px}

  /* right panel */
  .panel-right{position:absolute;left:800px;top:0;width:400px;height:566px;background:#fff}
  .landscape{position:absolute;inset:0}
  .brand{position:absolute;left:22px;top:24px;display:flex;flex-direction:column;color:var(--logo-blue)}
  .brand-name{font-size:22px;font-weight:700;letter-spacing:-.3px}
  .brand-sub{margin-top:6px;padding-top:3px;border-top:1px solid #9fb6d8;font-size:8px;color:#6f8fbf}
  .headline{position:absolute;left:36px;top:270px;width:340px;text-align:center;color:var(--white);
    font-weight:700;font-style:italic;font-size:29px;line-height:1.27;letter-spacing:.6px;
    text-shadow:2px 2px 2px rgba(40,60,90,.55)}
</style>
</head>
<body>
<div class="spread">

  <section class="panel-left">
    <div class="copy copy-top">
      <p><strong>Brightwell</strong> is considered one of Australia's leading <strong>Commercial Cleaning service provider</strong>, dedicated to delivering a quality service that adds value.</p>
      <p>Our business philosophy and international networks ensures we can deliver quality and cost effective cleaning solutions. Our highly skilled Management Team working across Australia and New Zealand has built a solid reputation maintaining the highest commercial cleaning standards.</p>
      <p>Brightwell's commitment to deliver quality is reflected in our rapidly growing clientele base and long term working relationships.</p>
      <p>Established in 1995 and initially servicing commercial and strata offices, Brightwell has progressively developed over 15 years to build a strong client network throughout Australia and New Zealand.</p>
    </div>
    <div class="tree-photo" role="img" aria-label="Photo of a large leafy green tree"></div>
    <div class="copy copy-bottom">
      <p>Brightwell now offers the highest commercial cleaning standards to commercial industry, retail and shopping centres, hotels and tertiary education facilities.</p>
      <p>Our continual commitment and dedication to delivering a quality service has enabled Brightwell to build a solid foundation and international presence.</p>
      <p>Building relationships based on ethical conduct towards employees and clientele defines our unique working environments and is a vital key to our success.</p>
    </div>
  </section>

  <section class="panel-middle">
    <div class="leaf-photo" role="img" aria-label="Close-up photo of fresh green leaves on a soft green background"></div>
    <p class="principles-intro">Our principle to put the client first, separates us from the rest<br>Engrained within each employee are five company principles of Brightwell.</p>
    <ul class="principles">
      <li><svg viewBox="0 0 12 12"><circle cx="6" cy="6" r="6" fill="#fff"/><path d="M3.2 6.2l1.9 1.9 3.8-4" fill="none" stroke="#4c8fe0" stroke-width="1.6"/></svg>Put the client first</li>
      <li><svg viewBox="0 0 12 12"><circle cx="6" cy="6" r="6" fill="#fff"/><path d="M3.2 6.2l1.9 1.9 3.8-4" fill="none" stroke="#4c8fe0" stroke-width="1.6"/></svg>Lead with integrity</li>
      <li><svg viewBox="0 0 12 12"><circle cx="6" cy="6" r="6" fill="#fff"/><path d="M3.2 6.2l1.9 1.9 3.8-4" fill="none" stroke="#4c8fe0" stroke-width="1.6"/></svg>Deliver a quality service</li>
      <li><svg viewBox="0 0 12 12"><circle cx="6" cy="6" r="6" fill="#fff"/><path d="M3.2 6.2l1.9 1.9 3.8-4" fill="none" stroke="#4c8fe0" stroke-width="1.6"/></svg>Take personal responsibility</li>
      <li><svg viewBox="0 0 12 12"><circle cx="6" cy="6" r="6" fill="#fff"/><path d="M3.2 6.2l1.9 1.9 3.8-4" fill="none" stroke="#4c8fe0" stroke-width="1.6"/></svg>Keep balance</li>
    </ul>
    <p class="principles-outro">Within these principles Brightwell has created a company that rewards dependability, integrity, safety and provides the training and development for all employees.</p>
    <div class="cert-box">
      <p class="cert-title">Brightwell Is ISO certified across 3 International Standards</p>
      <div class="cert-badges">
        <svg width="56" height="56" viewBox="0 0 56 56" role="img" aria-label="Quality certification badge"><circle cx="28" cy="28" r="26" fill="#fff" stroke="var(--cert-blue)" stroke-width="3"/></svg>
        <svg width="56" height="56" viewBox="0 0 56 56" role="img" aria-label="Environmental certification badge"><circle cx="28" cy="28" r="26" fill="#fff" stroke="var(--cert-green)" stroke-width="3"/></svg>
        <svg width="56" height="56" viewBox="0 0 56 56" role="img" aria-label="Safety certification badge"><circle cx="28" cy="28" r="26" fill="#fff" stroke="var(--cert-red)" stroke-width="3"/></svg>
      </div>
    </div>
  </section>

  <section class="panel-right">
    <svg class="landscape" width="400" height="566" viewBox="0 0 400 566" role="img" aria-label="Photo of a blue sky with clouds over a green coastal island and bay">
      <defs>
        <linearGradient id="scene" x1="0" y1="0" x2="0" y2="1">
          <stop offset="0" stop-color="#1f6fd0"/>
          <stop offset=".5" stop-color="#7fb8ea"/>
          <stop offset=".66" stop-color="#d9ecf6"/>
          <stop offset=".72" stop-color="#2f9fb8"/>
          <stop offset=".8" stop-color="#3e8a32"/>
          <stop offset="1" stop-color="#5fae2c"/>
        </linearGradient>
      </defs>
      <path d="M205 0 H400 V566 H0 V210 C70 150 150 80 205 0 Z" fill="url(#scene)"/>
    </svg>
    <div class="brand">
      <span class="brand-name">Brightwell</span>
      <span class="brand-sub">Environmental Cleaning Services</span>
    </div>
    <h1 class="headline">A Quality Service<br>That Adds Value</h1>
  </section>

</div>
</body>
</html>
```